The Timber Loft

We need a business card design for our wardrobe company.
Please visit our website www.zorvelcabinets.com to get an idea of who we are.

```html
<!DOCTYPE html>
<html lang="en">
<head>
<meta charset="utf-8">
<title>The Timber Loft — Business Card</title>
<link rel="stylesheet" href="https://fonts.googleapis.com/css2?family=Questrial&family=Oswald:wght@600&family=Libre+Baskerville&display=swap">
<style>
  :root {
    --teal-deep: #2aafb5;
    --teal-mid: #5fbfc5;
    --teal-soft: #b5dfe2;
    --teal-pale: #eef7f7;
    --ink: #1f2a2b;
    --ink-soft: #4b5a5c;
    --ink-body: #2e3536;
  }
  html, body {
    margin: 0;
    padding: 0;
    overflow: hidden;
    background: #ffffff;
  }
  .card {
    position: relative;
    width: 1200px;
    height: 800px;
    overflow: hidden;
    background:
      radial-gradient(circle at 100% 100%, var(--teal-pale) 0%, var(--teal-soft) 25%, var(--teal-mid) 55%, var(--teal-deep) 85%);
    font-family: "Questrial", sans-serif;
    color: var(--ink-body);
  }
  .card__arc {
    position: absolute;
    inset: 0;
  }
  .brand {
    position: absolute;
    left: 760px;
    top: 80px;
    display: flex;
    align-items: center;
    gap: 50px;
  }
  .brand__mark {
    width: 58px;
    height: 58px;
    background: var(--ink);
  }
  .brand__text {
    display: flex;
    flex-direction: column;
    gap: 8px;
  }
  .brand__name {
    font-size: 19px;
    letter-spacing: 0.5px;
    color: var(--ink);
    text-transform: uppercase;
  }
  .brand__tagline {
    font-size: 17px;
    color: var(--ink);
    padding-left: 18px;
  }
  .phone {
    position: absolute;
    left: 801px;
    top: 160px;
    font-size: 27px;
    color: var(--ink);
  }
  .headline {
    position: absolute;
    left: 0;
    right: 0;
    top: 283px;
    margin: 0;
    text-align: center;
    font-size: 49px;
    font-weight: 400;
    line-height: 67px;
    letter-spacing: 0.6px;
    color: var(--ink-soft);
    padding-left: 84px;
  }
  .location {
    position: absolute;
    left: 0;
    right: 0;
    top: 432px;
    margin: 0;
    text-align: center;
    font-size: 32px;
    line-height: 38px;
    color: var(--ink-soft);
    padding-left: 140px;
  }
  .team {
    position: absolute;
    top: 550px;
    left: 0;
    width: 1200px;
    height: 100px;
  }
  .member {
    position: absolute;
    top: 0;
    width: 300px;
    margin-left: -150px;
    text-align: center;
  }
  .member__name {
    font-family: "Oswald", sans-serif;
    font-weight: 600;
    font-size: 24px;
    line-height: 32px;
    color: var(--ink);
  }
  .member__role {
    margin-top: 4px;
    font-size: 19px;
    line-height: 24px;
    color: var(--ink-body);
  }
  .website {
    position: absolute;
    left: 0;
    right: 0;
    top: 694px;
    text-align: center;
    font-family: "Libre Baskerville", serif;
    font-size: 32px;
    letter-spacing: 10px;
    color: var(--ink-soft);
    padding-left: 32px;
  }
</style>
</head>
<body>
  <main class="card">
    <svg class="card__arc" width="1200" height="800" viewBox="0 0 1200 800" aria-hidden="true">
      <circle cx="-140" cy="440" r="866" fill="#ffffff" fill-opacity="0.3"/>
    </svg>

    <header class="brand">
      <div class="brand__mark"></div>
      <div class="brand__text">
        <span class="brand__name">The Timber Loft</span>
        <span class="brand__tagline">Built Right, Fitted Tight</span>
      </div>
    </header>
    <div class="phone">Call 0207 555 0148</div>

    <h1 class="headline">A bespoke fitted wardrobe company<br>that can also take care of the niggly stuff.</h1>
    <p class="location">Based in the heart of London</p>

    <section class="team">
      <div class="member" style="left:216px">
        <div class="member__name">Marcus Lindqvist</div>
        <div class="member__role">Head Honcho and Chief<br>Perfectionist</div>
      </div>
      <div class="member" style="left:485px">
        <div class="member__name">Tomas Varga</div>
        <div class="member__role">Cool-as-a-cucumber Installation<br>Manager</div>
      </div>
      <div class="member" style="left:741px">
        <div class="member__name">Elena Marin</div>
        <div class="member__role">Design Consultant and<br>Dream Maker</div>
      </div>
      <div class="member" style="left:972px">
        <div class="member__name">Ioana Radu</div>
        <div class="member__role">Design Consultant and<br>Dream Maker</div>
      </div>
    </section>

    <div class="website">www.zorvelcabinets.com</div>
  </main>
</body>
</html>
```